Orchard and Beacon Works: Problem to Solution Process

We need a powerpoint slide illustrating a process the begins with identifying a problem and proceed through various gates of potentially resolving the problem.
The attached file provides the steps a user must go through from point of recognizing they have a data need through resolving their problems are various stages.
This process is not yet in practice. It is a concept we are trying. We will use this slide to market the process while trying it with others.

Since the process is not yet in place, we need to visually communicate the theory we are implementing for users to quickly and easily understand. The resulting slide you are producing should tell the story of the user's path and the benefits for moving through this process. The slide with the process can include animation and / or videos to help demonstrate appropriately.
The largest benefit to the user is more immediate access to their data needs, to provide quicker insights and better decision making.
On the attached slide, the blue boxes are the processes we want to highlight. The text in the gray dotted boxes are intended to be informational for your purposes.
Each step 1- 4 should solve a user's problem. For example, if 100 problems are found, 50 should be resolved in step 1 and only 50 should move to step 2. Furthermore, only 30 should move to step 3 and 5 request should move to step 4. (Today, users go directly to step 4 for everything and it’s overwhelming to everyone!)

```html
<!DOCTYPE html>
<html lang="en">
<head>
<meta charset="utf-8">
<title>Our Process – Orchard and Beacon Works</title>
<link href="https://fonts.googleapis.com/css2?family=Lato:wght@400&display=swap" rel="stylesheet">
<style>
  :root {
    --page-bg: #eceff3;
    --slide-bg: #fdfdfe;
    --ink-title: #4a5876;
    --rule-accent: #4a5876;
    --node-light: #56647f;
    --node-dark: #2d374a;
    --node-ring: #f1f2f4;
    --node-text: #eef1f6;
    --connector: #a8b3c4;
    --chevron: #eceef1;
    --footer-rule: #d9dce1;
    --footer-muted: #9197a2;
    --footer-ink: #1d1f24;
  }
  * { box-sizing: border-box; margin: 0; padding: 0; }
  html, body { width: 1158px; height: 1200px; overflow: hidden; }
  body {
    background: var(--page-bg);
    font-family: "Lato", Arial, sans-serif;
    position: relative;
  }
  .slide-frame {
    position: absolute;
    left: 20px;
    top: 297px;
    width: 1118px;
    height: 606px;
    box-shadow: 0 18px 40px rgba(40, 50, 70, 0.25);
  }
  .slide {
    position: absolute;
    left: 0; top: 0;
    width: 1332px;
    height: 722px;
    transform: scale(0.8393);
    transform-origin: 0 0;
    background: var(--slide-bg);
    overflow: hidden;
  }
  .title-accent {
    position: absolute;
    left: 64px; top: 14px;
    width: 60px; height: 4px;
    background: var(--rule-accent);
  }
  .slide-title {
    position: absolute;
    left: 63px; top: 24px;
    font-size: 31px;
    font-weight: 400;
    color: var(--ink-title);
    letter-spacing: 0.2px;
  }
  .flow-lines {
    position: absolute;
    left: 0; top: 0;
  }
  .node {
    position: absolute;
    border-radius: 50%;
    background: var(--node-ring);
    box-shadow: 0 4px 10px rgba(40, 50, 70, 0.22);
    display: flex;
    align-items: center;
    justify-content: center;
  }
  .node-face {
    border-radius: 50%;
    background: linear-gradient(135deg, var(--node-light) 0%, #46536d 45%, var(--node-dark) 100%);
    width: calc(100% - 14px);
    height: calc(100% - 14px);
    display: flex;
    flex-direction: column;
    align-items: center;
    justify-content: center;
    text-align: center;
    color: var(--node-text);
    font-size: 16.5px;
    line-height: 1.5;
    padding: 0 10px;
  }
  .node-face .role { margin-top: 10px; }
  .node--large { width: 168px; height: 168px; }
  .node--small { width: 146px; height: 146px; }
  .node--small .node-face { font-size: 12.5px; line-height: 1.55; }
  .node--small .node-face .role { margin-top: 9px; }

  .footer-rule {
    position: absolute;
    left: 29px; top: 662px;
    width: 1274px; height: 1px;
    background: var(--footer-rule);
  }
  .brand {
    position: absolute;
    left: 25px; top: 688px;
    display: flex;
    align-items: center;
    gap: 9px;
    color: var(--footer-muted);
    font-size: 16px;
    letter-spacing: 3px;
    text-transform: uppercase;
  }
  .brand-mark {
    width: 18px; height: 18px;
    background: var(--footer-muted);
  }
  .confidential {
    position: absolute;
    left: 0; width: 1332px;
    top: 690px;
    text-align: center;
    font-size: 17px;
    color: var(--footer-ink);
  }
  .copyright {
    position: absolute;
    right: 91px; top: 688px;
    font-size: 16px;
    color: var(--footer-muted);
  }
</style>
</head>
<body>
  <div class="slide-frame">
    <section class="slide" aria-label="Our Process slide">
      <div class="title-accent"></div>
      <h1 class="slide-title">Our Process</h1>

      <svg class="flow-lines" width="1332" height="722" viewBox="0 0 1332 722" aria-hidden="true">
        <defs>
          <marker id="arrowhead" viewBox="0 0 6 6" refX="5" refY="3" markerWidth="6" markerHeight="6" orient="auto">
            <path d="M0,0.5 L5,3 L0,5.5" fill="none" stroke="var(--connector)" stroke-width="1"/>
          </marker>
        </defs>
        <g fill="none" stroke="var(--connector)" stroke-width="2" stroke-dasharray="5 4" marker-end="url(#arrowhead)">
          <line x1="274" y1="179" x2="421" y2="179"/>
          <line x1="593" y1="179" x2="740" y2="179"/>
          <line x1="911" y1="179" x2="1058" y2="179"/>
          <line x1="1144" y1="265" x2="1144" y2="295"/>
          <polyline points="825,265 825,370 1068,370"/>
          <line x1="1144" y1="444" x2="1144" y2="477"/>
          <line x1="1058" y1="562" x2="593" y2="562"/>
          <line x1="421" y1="562" x2="274" y2="562"/>
        </g>
        <g fill="var(--chevron)">
          <path d="M168,290 L188,270 L208,290 L208,324 L188,306 L168,324 Z"/>
          <path d="M168,360 L188,340 L208,360 L208,394 L188,376 L168,394 Z"/>
          <path d="M168,430 L188,410 L208,430 L208,464 L188,446 L168,464 Z"/>
        </g>
      </svg>

      <div class="node node--large" style="left:104px; top:95px;">
        <div class="node-face">User to communicate the problem they are trying to solve</div>
      </div>
      <div class="node node--large" style="left:423px; top:95px;">
        <div class="node-face"><span>Self<br>Service</span><span class="role">End User</span></div>
      </div>
      <div class="node node--large" style="left:741px; top:95px;">
        <div class="node-face"><span>Super User<br>Or Problem<br>Definition Creation<br>Super User</span></div>
      </div>
      <div class="node node--large" style="left:1060px; top:95px;">
        <div class="node-face"><span>Worked within<br>Agile</span><span class="role">BI teams</span></div>
      </div>
      <div class="node node--small" style="left:1071px; top:297px;">
        <div class="node-face"><span>Problem Solving to<br>Define problem</span><span class="role">Super User</span></div>
      </div>
      <div class="node node--large" style="left:104px; top:478px;">
        <div class="node-face"><span>Gain insights</span><span class="role">End User</span></div>
      </div>
      <div class="node node--large" style="left:423px; top:478px;">
        <div class="node-face"><span>Check Benefits</span><span class="role">BI teams</span></div>
      </div>
      <div class="node node--large" style="left:1060px; top:478px;">
        <div class="node-face"><span>Project Design &amp;<br>Execute</span><span class="role">BI/EA teams</span></div>
      </div>

      <div class="footer-rule"></div>
      <div class="brand"><span class="brand-mark"></span><span>Orchard and Beacon Works</span></div>
      <div class="confidential">Confidential</div>
      <div class="copyright">© Orchard and Beacon Works</div>
    </section>
  </div>
</body>
</html>
```